Pharmacist turned chef in Key West Fl needs a logo design

I am looking for a professional looking business card that says who I am and what I do. For example Chef Dale Morrow, natural organic and health supportive cooking. Phone 305-617-4289 email dalemorrow@quillpost.example web www.thehearthremedy.example, Key West fl. The color or colors should have some green and other colors that look good together that stimulate appetite and give a clean healthy image. To help with a thought process, words like food as medicine, medicine is food, good nutrition is health but at the same time I do not want a lot of medical symbols that me it look clinical. Any questions please contact me.

```html
<!DOCTYPE html>
<html lang="en">
<head>
<meta charset="utf-8">
<title>Chef Dale Morrow – Business Card</title>
<link rel="stylesheet" href="https://fonts.googleapis.com/css2?family=Questrial&family=Source+Sans+3:wght@400&display=swap">
<style>
  :root {
    --page-bg: #ffffff;
    --card-black: #000000;
    --leaf-green: #22c000;
    --text-white: #ffffff;
  }
  html, body {
    margin: 0;
    padding: 0;
    width: 1200px;
    height: 1000px;
    overflow: hidden;
    background: var(--page-bg);
  }
  .business-card {
    display: block;
    width: 1200px;
    height: 1000px;
  }
  .card-accent { fill: var(--leaf-green); }
  .card-field { fill: var(--card-black); }
  .rule { fill: var(--text-white); }
  .chef-name {
    font-family: "Questrial", "Century Gothic", sans-serif;
    font-size: 104px;
    fill: var(--leaf-green);
  }
  .tagline, .website, .contact-line {
    font-family: "Source Sans 3", "Myriad Pro", sans-serif;
    fill: var(--text-white);
  }
  .tagline { font-size: 39px; }
  .website { font-size: 32px; }
  .contact-line { font-size: 32px; }
</style>
</head>
<body>
<svg class="business-card" viewBox="0 0 1200 1000" xmlns="http://www.w3.org/2000/svg" role="img" aria-label="Business card for Chef Dale Morrow, natural organic and health supportive cooking, Key West, Florida">
  <rect class="card-accent" x="77" y="211" width="1046" height="598"/>
  <path class="card-field" d="M77 430 C150 290 300 225 460 211 L1123 211 L1123 590 C1080 700 950 785 785 809 L77 809 Z"/>

  <text class="website" x="1082" y="275" text-anchor="end">www.thehearthremedy.example</text>

  <rect class="rule" x="296" y="400" width="748" height="6"/>
  <text class="chef-name" x="208" y="507" textLength="836" lengthAdjust="spacingAndGlyphs">Chef Dale Morrow</text>
  <rect class="rule" x="208" y="545" width="836" height="6"/>

  <text class="tagline" x="207" y="597" textLength="837" lengthAdjust="spacingAndGlyphs">Natural Organic &amp; Health Supportive Cooking</text>

  <text class="contact-line" x="117" y="670">Key West, FL</text>
  <text class="contact-line" x="117" y="715">Phone: (305) 617-4289</text>
  <text class="contact-line" x="117" y="760">E-mail: dalemorrow@quillpost.example</text>
</svg>
</body>
</html>
```